Beautify our counselling web application

I have a web application in development and at the moment it is very plain.
It has being developed with laravel and vue. I need a simple design for the user interface to make it look more sleek and professional. I will need someone who is able to code the design as part of the service. The app is very low-cost for voluntary and social enterprise services and we don't have a lot of money so I need someone who is just starting out or someone with a big heart.
I have uploaded current pages to show the contents.
I will tip for good work.

Target Market(s)

Counsellors and psychotherapists

Industry/Entity Type

SaaS

Font styles to use
Serif
Sans Serif

Colors
0054AA
0677BA
7BADD7
CADEEF
E8F1F8

Requirements
Must have
• Ability to code the design into the current site
Nice to have
• elegant, modern. cool, profession. nice examples include brintaloft.com quelvanote.com morvend.com
Should not have
• corny literal 90s icons, icons with more than one colour using primary colours

```html
<!DOCTYPE html>
<html lang="en">
<head>
<meta charset="utf-8">
<title>Caseload</title>
<link href="https://fonts.googleapis.com/css2?family=Inter:wght@400;500&display=swap" rel="stylesheet">
<style>
:root{
  --brand:#0054AA;
  --brand-mid:#0677BA;
  --brand-soft:#CADEEF;
  --brand-tint:#E8F1F8;
  --page:#F5F7FA;
  --panel:#FFFFFF;
  --ink:#1F2328;
  --ink-soft:#3F4750;
  --muted:#5B636D;
  --line:#E6E9EE;
  --risk:#1DB878;
}
*{box-sizing:border-box;margin:0;padding:0}
html,body{width:1200px;height:853px;overflow:hidden}
body{font-family:"Inter",sans-serif;background:var(--page);color:var(--ink);position:relative}
.sidebar{position:absolute;left:0;top:0;width:208px;height:853px;background:var(--panel)}
.nav-item{position:absolute;left:0;width:208px;height:35px;display:flex;align-items:center;font-size:13.5px;color:var(--ink-soft)}
.nav-item svg{position:absolute;left:37px;width:16px;height:16px;stroke:var(--ink-soft);fill:none;stroke-width:1.6}
.nav-item span{position:absolute;left:65px}
.nav-item.active{background:var(--brand-tint);color:var(--ink);font-weight:500;border-right:2px solid var(--brand)}
.nav-item.active svg{stroke:var(--brand)}
.top-actions svg{position:absolute;top:22px;width:18px;height:18px}
.page-title{position:absolute;left:229px;top:48px;font-size:23px;font-weight:400;color:var(--ink)}
.filter{position:absolute;left:228px;top:131px;width:77px;height:34px;background:var(--panel);border-radius:3px 0 0 3px;font-size:12px;display:flex;align-items:center;padding-left:14px;gap:6px}
.search{position:absolute;left:307px;top:131px;width:156px;height:34px;background:var(--panel);border-radius:0 3px 3px 0;font-size:12px;color:#C3C8CE;display:flex;align-items:center;padding-left:23px}
.caseload-table{position:absolute;left:228px;top:177px;width:964px;background:var(--panel);border-radius:4px}
.row{display:grid;grid-template-columns:44px 68px 131px 65px 127px 65px 121px 111px 123px 79px;padding-left:15px;height:44px;align-items:center;border-top:1px solid var(--line);font-size:12px;color:var(--ink-soft)}
.row.head{height:37px;border-top:none;font-size:10px;color:var(--ink-soft)}
.dot{width:6px;height:6px;border-radius:50%;background:var(--risk);margin-left:5px}
.client{color:var(--brand-mid)}
.pill{width:62px;height:18px;border:1px solid #C9CED5;border-radius:9px;font-size:10px;display:flex;align-items:center;padding-left:7px;gap:5px;color:var(--ink-soft)}
.pill svg{width:8px;height:8px;margin-left:2px}
</style>
</head>
<body>
<aside class="sidebar">
  <div class="nav-item" style="top:56px"><svg viewBox="0 0 16 16"><rect x="2" y="2" width="5" height="6"/><rect x="9" y="2" width="5" height="3"/><rect x="2" y="10" width="5" height="4"/><rect x="9" y="7" width="5" height="7"/></svg><span>Dashboard</span></div>
  <div class="nav-item active" style="top:105px"><svg viewBox="0 0 16 16"><rect x="2" y="4" width="12" height="10"/><path d="M6 4V2h4v2M7 7l2 2-2 2"/></svg><span>Caseload</span></div>
  <div class="nav-item" style="top:154px"><svg viewBox="0 0 16 16"><rect x="2" y="3" width="12" height="11"/><path d="M2 6h12M5 1v3M11 1v3"/></svg><span>Calendar</span></div>
  <div class="nav-item" style="top:203px"><svg viewBox="0 0 16 16"><circle cx="6" cy="6" r="2.5"/><path d="M1.5 13c0-2.5 2-4 4.5-4s4.5 1.5 4.5 4zM10 3.5a2.5 2.5 0 010 5M12 9.5c1.5.5 2.5 1.8 2.5 3.5"/></svg><span>Users</span></div>
  <div class="nav-item" style="top:252px"><svg viewBox="0 0 16 16"><circle cx="8" cy="8" r="5.5"/><circle cx="8" cy="8" r="2.5"/><path d="M3 13l10-10"/></svg><span>Services</span></div>
  <div class="nav-item" style="top:301px"><svg viewBox="0 0 16 16"><circle cx="8" cy="6" r="2"/><circle cx="3.5" cy="7" r="1.5"/><circle cx="12.5" cy="7" r="1.5"/><path d="M4.5 12c0-2 1.5-3 3.5-3s3.5 1 3.5 3zM1 12c0-1.5.8-2.3 2.2-2.5M15 12c0-1.5-.8-2.3-2.2-2.5"/></svg><span>Clients</span></div>
  <div class="nav-item" style="top:350px"><svg viewBox="0 0 16 16"><path d="M2 4l1.5 1.5L6 3M2 10l1.5 1.5L6 9M8 4.5h6M8 10.5h6"/></svg><span>Audit</span></div>
  <div class="nav-item" style="top:399px"><svg viewBox="0 0 16 16"><rect x="2" y="3" width="12" height="9"/><path d="M5 14h6M5 9h6"/></svg><span>Monitoring</span></div>
  <div class="nav-item" style="top:448px"><svg viewBox="0 0 16 16"><rect x="2" y="2" width="12" height="12"/><path d="M7 2v12M7 8h7"/></svg><span>Templates</span></div>
</aside>

<div class="top-actions">
  <svg viewBox="0 0 18 18" style="left:1089px"><circle cx="9" cy="9" r="8.5" fill="var(--brand)"/><path d="M6.8 7a2.2 2.2 0 114 1.2c-.8.7-1.6 1-1.6 2.1" stroke="#fff" stroke-width="1.6" fill="none" stroke-linecap="round"/><circle cx="9.2" cy="13.2" r=".9" fill="#fff"/></svg>
  <svg viewBox="0 0 18 18" style="left:1131px" fill="none" stroke="var(--brand)" stroke-width="1.7"><circle cx="9" cy="9" r="7.8"/><circle cx="9" cy="7.3" r="2.6"/><path d="M4.2 14.2c1.2-1.8 2.8-2.6 4.8-2.6s3.6.8 4.8 2.6"/></svg>
  <svg viewBox="0 0 18 18" style="left:1169px" fill="none" stroke="var(--brand)" stroke-width="1.7" stroke-linecap="round"><path d="M7 2.5H3v13h4M8 9h8M13 6l3 3-3 3"/></svg>
</div>

<h1 class="page-title">Caseload</h1>
<div class="filter">Filter <svg width="10" height="7" viewBox="0 0 10 7"><path d="M1 1l4 4 4-4" stroke="#1F2328" stroke-width="1.5" fill="none"/></svg></div>
<div class="search">Search</div>

<div class="caseload-table">
  <div class="row head"><span>Risk</span><span>Alerts</span><span>Client</span><span>ID</span><span>Service</span><span>Therapist</span><span>Date of referral</span><span>First Contact</span><span>Previous Episode</span><span>Contacts</span></div>
  <div class="row"><i class="dot"></i><span></span><span class="client">Owen Farley</span><span>002</span><span>Demo Service 1</span><span>Paul</span><span>12/02/2023</span><span>12/02/2023</span><span>12/02/2023</span><span class="pill">Total 2<svg viewBox="0 0 8 8"><path d="M1 2.5l3 3 3-3" stroke="#1F2328" stroke-width="1.5" fill="none"/></svg></span></div>
  <div class="row"><i class="dot"></i><span></span><span class="client">Owen Farley</span><span>002</span><span>Demo Service 1</span><span>Paul</span><span>12/02/2023</span><span>12/02/2023</span><span>12/02/2023</span><span class="pill">Total 2<svg viewBox="0 0 8 8"><path d="M1 2.5l3 3 3-3" stroke="#1F2328" stroke-width="1.5" fill="none"/></svg></span></div>
  <div class="row"><i class="dot"></i><span></span><span class="client">Owen Farley</span><span>002</span><span>Demo Service 1</span><span>Paul</span><span>12/02/2023</span><span>12/02/2023</span><span>12/02/2023</span><span class="pill">Total 2<svg viewBox="0 0 8 8"><path d="M1 2.5l3 3 3-3" stroke="#1F2328" stroke-width="1.5" fill="none"/></svg></span></div>
  <div class="row"><i class="dot"></i><span></span><span class="client">Owen Farley</span><span>002</span><span>Demo Service 1</span><span>Paul</span><span>12/02/2023</span><span>12/02/2023</span><span>12/02/2023</span><span class="pill">Total 2<svg viewBox="0 0 8 8"><path d="M1 2.5l3 3 3-3" stroke="#1F2328" stroke-width="1.5" fill="none"/></svg></span></div>
  <div class="row"><i class="dot"></i><span></span><span class="client">Owen Farley</span><span>002</span><span>Demo Service 1</span><span>Paul</span><span>12/02/2023</span><span>12/02/2023</span><span>12/02/2023</span><span class="pill">Total 2<svg viewBox="0 0 8 8"><path d="M1 2.5l3 3 3-3" stroke="#1F2328" stroke-width="1.5" fill="none"/></svg></span></div>
  <div class="row"><i class="dot"></i><span></span><span class="client">Owen Farley</span><span>002</span><span>Demo Service 1</span><span>Paul</span><span>12/02/2023</span><span>12/02/2023</span><span>12/02/2023</span><span class="pill">Total 2<svg viewBox="0 0 8 8"><path d="M1 2.5l3 3 3-3" stroke="#1F2328" stroke-width="1.5" fill="none"/></svg></span></div>
  <div class="row"><i class="dot"></i><span></span><span class="client">Owen Farley</span><span>002</span><span>Demo Service 1</span><span>Paul</span><span>12/02/2023</span><span>12/02/2023</span><span>12/02/2023</span><span class="pill">Total 2<svg viewBox="0 0 8 8"><path d="M1 2.5l3 3 3-3" stroke="#1F2328" stroke-width="1.5" fill="none"/></svg></span></div>
  <div class="row"><i class="dot"></i><span></span><span class="client">Owen Farley</span><span>002</span><span>Demo Service 1</span><span>Paul</span><span>12/02/2023</span><span>12/02/2023</span><span>12/02/2023</span><span class="pill">Total 2<svg viewBox="0 0 8 8"><path d="M1 2.5l3 3 3-3" stroke="#1F2328" stroke-width="1.5" fill="none"/></svg></span></div>
  <div class="row"><i class="dot"></i><span></span><span class="client">Owen Farley</span><span>002</span><span>Demo Service 1</span><span>Paul</span><span>12/02/2023</span><span>12/02/2023</span><span>12/02/2023</span><span class="pill">Total 2<svg viewBox="0 0 8 8"><path d="M1 2.5l3 3 3-3" stroke="#1F2328" stroke-width="1.5" fill="none"/></svg></span></div>
  <div class="row"><i class="dot"></i><span></span><span class="client">Owen Farley</span><span>002</span><span>Demo Service 1</span><span>Paul</span><span>12/02/2023</span><span>12/02/2023</span><span>12/02/2023</span><span class="pill">Total 2<svg viewBox="0 0 8 8"><path d="M1 2.5l3 3 3-3" stroke="#1F2328" stroke-width="1.5" fill="none"/></svg></span></div>
  <div class="row"><i class="dot"></i><span></span><span class="client">Owen Farley</span><span>002</span><span>Demo Service 1</span><span>Paul</span><span>12/02/2023</span><span>12/02/2023</span><span>12/02/2023</span><span class="pill">Total 2<svg viewBox="0 0 8 8"><path d="M1 2.5l3 3 3-3" stroke="#1F2328" stroke-width="1.5" fill="none"/></svg></span></div>
  <div class="row"><i class="dot"></i><span></span><span class="client">Owen Farley</span><span>002</span><span>Demo Service 1</span><span>Paul</span><span>12/02/2023</span><span>12/02/2023</span><span>12/02/2023</span><span class="pill">Total 2<svg viewBox="0 0 8 8"><path d="M1 2.5l3 3 3-3" stroke="#1F2328" stroke-width="1.5" fill="none"/></svg></span></div>
  <div class="row"><i class="dot"></i><span></span><span class="client">Owen Farley</span><span>002</span><span>Demo Service 1</span><span>Paul</span><span>12/02/2023</span><span>12/02/2023</span><span>12/02/2023</span><span class="pill">Total 2<svg viewBox="0 0 8 8"><path d="M1 2.5l3 3 3-3" stroke="#1F2328" stroke-width="1.5" fill="none"/></svg></span></div>
  <div class="row"><i class="dot"></i><span></span><span class="client">Owen Farley</span><span>002</span><span>Demo Service 1</span><span>Paul</span><span>12/02/2023</span><span>12/02/2023</span><span>12/02/2023</span><span class="pill">Total 2<svg viewBox="0 0 8 8"><path d="M1 2.5l3 3 3-3" stroke="#1F2328" stroke-width="1.5" fill="none"/></svg></span></div>
</div>
</body>
</html>
```